Residential Construction Company needs flyer designed.

We need a flyer design for a residential Rain Gutter and Screen room company. We have over 50 years in the remodeling industry and service all of Middle Georgia. We want the brochure to highlight our wonderful managerial staff to our great instillation crews. We also want to showcase the high-quality products that we use, gutter, leaf protection, screen rooms and sunrooms and the quality craftsmanship homeowners will receive when they choose to go with our company.

```html
<!DOCTYPE html>
<html lang="en">
<head>
<meta charset="utf-8">
<title>Hartwell Gutters &amp; Exteriors – Flyer</title>
<link rel="stylesheet" href="https://fonts.googleapis.com/css2?family=Montserrat:wght@800&family=Open+Sans:wght@400;500;600&family=Raleway:wght@500;700;800&family=Poppins:ital,wght@1,700&display=swap">
<style>
:root{
  --navy:#1f2c58;
  --blue:#1a6fb8;
  --indigo:#2b2f82;
  --teal:#22b39c;
  --ink:#2a2a2a;
  --paper:#ffffff;
  --card:#f7f6f9;
  --backdrop:#e6e6e6;
}
*{margin:0;padding:0;box-sizing:border-box}
html,body{width:1200px;height:1200px;overflow:hidden;background:var(--backdrop)}
.flyer{position:absolute;left:136px;top:0;width:927px;height:1200px;background:var(--paper);font-family:"Open Sans",sans-serif;overflow:hidden}
.hero-photo{position:absolute;left:26px;top:32px;width:875px;height:546px;border-radius:0 36px 0 0;
  background:linear-gradient(180deg,#9db8d8 0%,#c9d6e4 22%,#5b6068 40%,#d8d6cf 55%,#cfcbc1 72%,#4f6a3a 88%,#6f8a4a 100%)}
.hero-shade{position:absolute;left:26px;top:32px;width:500px;height:546px;background:linear-gradient(90deg,rgba(20,30,40,.45),rgba(20,30,40,0))}
.brand-panel{position:absolute;left:0;top:0;width:372px;height:163px;background:var(--paper);border-radius:0 0 34px 0}
.brand{position:absolute;left:48px;top:58px;display:flex;align-items:center;gap:10px;font-family:"Raleway",sans-serif;font-weight:800;font-size:25px;color:var(--blue);line-height:1.05}
.brand-dot{width:34px;height:34px;border-radius:50%;background:var(--blue);flex:none}
.hero-kicker{position:absolute;left:67px;top:218px;font-family:"Raleway",sans-serif;font-weight:500;font-size:37px;color:#fff;letter-spacing:.5px}
.hero-title{position:absolute;left:64px;top:250px;font-family:"Montserrat",sans-serif;font-weight:800;font-size:100px;color:#fff;letter-spacing:-1px;line-height:1}
.hero-sub{position:absolute;left:67px;top:355px;font-weight:600;font-size:18px;color:#fff}
.navy-band{position:absolute;left:26px;top:578px;width:875px;height:502px;background:var(--navy);border-radius:0 0 30px 30px;overflow:hidden}
.guard-photo{position:absolute;right:0;top:0;width:380px;height:502px;clip-path:polygon(24% 0,100% 0,100% 100%,0 100%);
  background:linear-gradient(160deg,#1b2a6a 0%,#2346a8 45%,#1a3a8c 70%,#0f1d4a 100%)}
.services-card{position:absolute;left:49px;top:480px;width:829px;height:349px;background:var(--card);border-radius:26px}
.services-tab{position:absolute;left:279px;top:448px;width:366px;height:58px;background:var(--blue);border-radius:6px;
  color:#fff;font-family:"Raleway",sans-serif;font-size:51px;line-height:58px;text-align:center;font-weight:500}
.services-tab b{font-weight:800}
.service{position:absolute;top:517px;width:272px;text-align:center}
.service-icon{width:44px;height:44px;border-radius:50%;background:var(--indigo);margin:0 auto;display:flex;align-items:center;justify-content:center}
.service-name{font-family:"Raleway",sans-serif;font-weight:700;font-size:29px;color:var(--indigo);margin-top:2px}
.service-desc{font-size:13px;color:var(--ink);line-height:15px;margin-top:3px}
.service-photo{position:absolute;top:657px;width:252px;height:155px;border:3px solid var(--blue);border-radius:10px}
.photo-gutters{left:67px;background:linear-gradient(180deg,#dfe6ee 0%,#4a4e58 25%,#b9a99a 55%,#8e7c6c 100%)}
.photo-patio{left:338px;background:linear-gradient(180deg,#9aa0a8 0%,#d9dcde 30%,#f0f0ee 55%,#4f5a3e 100%)}
.photo-screen{left:611px;background:linear-gradient(160deg,#8d8f92 0%,#6e7074 40%,#9a8a78 70%,#7d6c5c 100%)}
.install-heading{position:absolute;left:77px;top:840px;font-family:"Poppins",sans-serif;font-style:italic;font-weight:700;font-size:32px;line-height:41px;color:#fff}
.install-heading em{color:var(--teal);font-style:italic}
.install-list{position:absolute;left:0;top:0;list-style:none;color:#fff;font-size:18.5px;font-weight:500;line-height:23px}
.install-list li{position:absolute;white-space:nowrap;padding-left:27px}
.install-list svg{position:absolute;left:0;top:2px}
.partners-label{position:absolute;left:59px;top:1096px;font-size:17px;color:var(--indigo);padding-bottom:4px;border-bottom:1px solid var(--indigo)}
.partner-badges{position:absolute;left:59px;top:1140px;display:flex;align-items:center;gap:14px}
.badge-round{width:42px;height:42px;border-radius:50%;background:#8a8a8a}
.badge-rect{width:72px;height:22px;border-radius:3px;background:#8a94b8}
.badge-rect.red{background:#d9483b}
.call-label{position:absolute;right:37px;top:1090px;font-family:"Raleway",sans-serif;font-weight:500;font-size:26px;color:var(--indigo);display:flex;align-items:center;gap:6px}
.call-number{position:absolute;right:33px;top:1128px;font-family:"Raleway",sans-serif;font-weight:700;font-size:52px;color:var(--indigo);letter-spacing:-.5px}
</style>
</head>
<body>
<main class="flyer">
  <div class="hero-photo" role="img" aria-label="Photo of a large white stone house with a dark slate roof, trees and landscaped lawn"></div>
  <div class="hero-shade"></div>
  <div class="brand-panel">
    <div class="brand"><span class="brand-dot"></span><span>Hartwell Gutters<br>&amp; Exteriors</span></div>
  </div>
  <p class="hero-kicker">START YOUR HOME</p>
  <h1 class="hero-title">RENEWAL</h1>
  <p class="hero-sub">WE HAVE MORE THAN 20 YEARS OF EXPERIANCES</p>

  <div class="navy-band">
    <div class="guard-photo" role="img" aria-label="Close-up photo of a blue perforated gutter guard on a roof edge"></div>
  </div>

  <section class="services-card"></section>
  <h2 class="services-tab"><b>Our</b> Services</h2>

  <div class="service" style="left:57px">
    <div class="service-icon"><svg width="26" height="26" viewBox="0 0 26 26" fill="none" stroke="#fff" stroke-width="2"><path d="M4 10h18l-3 10H7z"/><path d="M8 6l14 4"/></svg></div>
    <div class="service-name">Gutter Systems</div>
    <p class="service-desc">Avoid Water Damage<br>with Proper Drainage</p>
  </div>
  <div class="service" style="left:328px">
    <div class="service-icon"><svg width="28" height="26" viewBox="0 0 28 26" fill="none" stroke="#fff" stroke-width="2"><path d="M3 8h22l-2 6H5z"/><path d="M7 14v6M21 14v6M11 9l-2 5M16 9l-2 5M21 9l-2 5"/></svg></div>
    <div class="service-name">Patio Covers</div>
    <p class="service-desc">Built for entertaining and<br>shelter from the sun</p>
  </div>
  <div class="service" style="left:601px">
    <div class="service-icon"><svg width="26" height="26" viewBox="0 0 26 26" fill="none" stroke="#fff" stroke-width="2"><path d="M3 13L13 4l10 9"/><path d="M6 11v11h14V11"/><path d="M10 22v-6h6v6"/></svg></div>
    <div class="service-name">Screenroom</div>
    <p class="service-desc">Enjoy Your Patio with<br>a Screen Room</p>
  </div>

  <div class="service-photo photo-gutters" role="img" aria-label="Photo of a brick home with an arched screened porch"></div>
  <div class="service-photo photo-patio" role="img" aria-label="Photo of a white enclosed patio room with screen panels"></div>
  <div class="service-photo photo-screen" role="img" aria-label="Photo of a roof edge with a gutter cover over brick wall"></div>

  <h3 class="install-heading">We are <em>specializes</em> in the quality<br>installation of</h3>
  <ul class="install-list">
    <li style="left:74px;top:943px"><svg width="20" height="20" viewBox="0 0 20 20" fill="none" stroke="#fff" stroke-width="2"><rect x="1.5" y="3.5" width="15" height="15" rx="2"/><path d="M5 10l4 4 9-11"/></svg>Clearflo Gutter Protection System</li>
    <li style="left:74px;top:980px"><svg width="20" height="20" viewBox="0 0 20 20" fill="none" stroke="#fff" stroke-width="2"><rect x="1.5" y="3.5" width="15" height="15" rx="2"/><path d="M5 10l4 4 9-11"/></svg>Seamless Aluminum Gutters<br>&amp; Downspouts</li>
    <li style="left:74px;top:1038px"><svg width="20" height="20" viewBox="0 0 20 20" fill="none" stroke="#fff" stroke-width="2"><rect x="1.5" y="3.5" width="15" height="15" rx="2"/><path d="M5 10l4 4 9-11"/></svg>Gutter Cleaning</li>
    <li style="left:446px;top:943px"><svg width="20" height="20" viewBox="0 0 20 20" fill="none" stroke="#fff" stroke-width="2"><rect x="1.5" y="3.5" width="15" height="15" rx="2"/><path d="M5 10l4 4 9-11"/></svg>Patio Covers</li>
    <li style="left:446px;top:980px"><svg width="20" height="20" viewBox="0 0 20 20" fill="none" stroke="#fff" stroke-width="2"><rect x="1.5" y="3.5" width="15" height="15" rx="2"/><path d="M5 10l4 4 9-11"/></svg>Gutter Covers</li>
  </ul>

  <p class="partners-label">Our Partnetrs</p>
  <div class="partner-badges" aria-label="Partner badges">
    <span class="badge-round"></span>
    <span class="badge-rect"></span>
    <span class="badge-rect"></span>
    <span class="badge-rect red"></span>
  </div>

  <p class="call-label"><svg width="22" height="22" viewBox="0 0 24 24" fill="none" stroke="currentColor" stroke-width="2"><path d="M5 3h4l2 5-3 2a12 12 0 0 0 6 6l2-3 5 2v4a2 2 0 0 1-2 2A18 18 0 0 1 3 5a2 2 0 0 1 2-2z"/></svg>Call us today</p>
  <p class="call-number">(555) 014-2870</p>
</main>
</body>
</html>
```